Lanterns and lemonades - fun, casual event near the beach to raise money for needy families

We are seeking a logo, invitation and save the date for our charity event called "Lanterns and Lemonades" set to occur on Dec 1,2017. We want to use the logo on letterhead, social media, etc.

Officially formed in 1955, our all-volunteer organization fundraises to offer a unique service in our area - providing one-time emergency assistance for those experiencing an unexpected temporary downturn.

Referrals come to us from governmental or private social service organizations as well as churches and temples. We work with social service professionals who have developed plans with their clients so they can get back on their feet after receiving our assistance. We have developed an extensive network of professionals in the community upon whom we can rely - and who in turn depend upon us for stopgap funding.

We are there when all other alternatives have been exhausted and immediate help is needed. We provide emergency assistance to those with a recovery plan in place and a goal of financial stability and thereby improving the quality of life for children, the elderly, single men and women and families in our area.

Target Market(s)

Age 35-65 affluent couples

Industry/Entity Type

Charity

Font styles to use
Decorative
Script

Colors

Designer to choose colors to be used in the design.

Requirements
Must have
• Image of margaritas and holiday themeno specific mention of "Christmas" no specific mention of "Christmas"
Nice to have
• Maybe beach-ish or water theme. Event will be at a rooftop bar along the beach.
Should not have
• no specific mention of "Christmas"

```html
<!DOCTYPE html>
<html lang="en">
<head>
<meta charset="utf-8">
<title>Save to Date – Lanterns &amp; Lemonades</title>
<link href="https://fonts.googleapis.com/css2?family=Great+Vibes&family=Playfair+Display:wght@400;900&display=swap" rel="stylesheet">
<style>
  :root {
    --paper: #f6f5f1;
    --ink: #2f2f2f;
    --ink-soft: #6b6b6b;
    --wash-teal: #cfe8e4;
    --wash-mint: #dcefe9;
    --wash-blue: #bfd0e6;
    --wash-lilac: #c3c3e0;
    --leaf: #8f9a4e;
  }
  html, body {
    margin: 0;
    padding: 0;
    overflow: hidden;
    background: var(--paper);
  }
  .card {
    position: relative;
    width: 857px;
    height: 1200px;
    overflow: hidden;
    background: var(--paper);
  }
  .watercolor-wash {
    position: absolute;
    inset: 0;
    background:
      radial-gradient(ellipse 70% 30% at 20% 78%, var(--wash-mint) 0%, rgba(220,239,233,0) 70%),
      radial-gradient(ellipse 60% 25% at 75% 72%, var(--wash-teal) 0%, rgba(207,232,228,0) 70%),
      radial-gradient(ellipse 80% 20% at 50% 100%, var(--wash-lilac) 0%, rgba(195,195,224,0) 75%),
      linear-gradient(to bottom, rgba(207,232,228,0) 0%, rgba(207,232,228,0) 55%, var(--wash-teal) 72%, var(--wash-blue) 90%, var(--wash-lilac) 100%);
  }
  .headline {
    position: absolute;
    left: 0;
    right: 0;
    top: 432px;
    margin: 0;
    text-align: center;
    font-family: "Great Vibes", cursive;
    font-weight: 400;
    font-size: 104px;
    line-height: 1;
    color: var(--ink);
  }
  .event-name {
    position: absolute;
    left: 0;
    right: 0;
    top: 553px;
    margin: 0;
    text-align: center;
    font-family: "Playfair Display", serif;
    font-size: 34px;
    line-height: 1.2;
    color: var(--ink-soft);
  }
  .event-date {
    position: absolute;
    left: 0;
    right: 0;
    top: 610px;
    margin: 0;
    text-align: center;
    font-family: "Playfair Display", serif;
    font-weight: 900;
    font-size: 58px;
    line-height: 1.2;
    letter-spacing: 2px;
    font-variant-numeric: lining-nums;
    color: var(--ink);
  }
  .mistletoe-sprig {
    position: absolute;
    left: 345px;
    top: 757px;
    width: 185px;
    height: 178px;
    border-radius: 50%;
    background: radial-gradient(ellipse at 45% 45%, rgba(143,154,78,0.75) 0%, rgba(143,154,78,0.35) 45%, rgba(143,154,78,0) 70%);
  }
</style>
</head>
<body>
  <main class="card">
    <div class="watercolor-wash"></div>

    <h1 class="headline">Save to Date</h1>
    <p class="event-name">Lanterns &amp; Lemonades</p>
    <p class="event-date">1 DEC, 2017</p>

    <div class="mistletoe-sprig" role="img" aria-label="Watercolour sprig of mistletoe with green leaves and white berries"></div>
  </main>
</body>
</html>
```